MOSLEN Environmental needs an upgrade to its current business cards design

We need an upgrade to our current business cards design, where the MOSLEN acronym is included, as possible and not being overloaded.
MOSLEN Environmental is an Environmental Consultancy Firm based in Sydney.
We would like to see creative designs different from the standard type of business cards (for example, rounded edges, different to standard size of common business cards.

Target Market(s)

industrial companies (oil & gas, petrochemical, mining, insolvency, finance and manufacturing), developers, architect firms, law firms.

Industry/Entity Type

Business

Contact Information for Business Card

logos (brand and acronym), if they don't appear overloaded.
name
role
name of company (MOSLEN Environmental),
address (Level 3, Suite 3C, 47-49 Dorrigan Lane, Wexmoor, NSW, 2188) landline (02 7314 2986)
mobile (staff member)
email (staff member) and
website (www.moslengreen.example).
Include: Contaminated Land, Site Remediation, Groundwater Assessment, Health and Ecological Risk Assessments, Acid Sulfate Soils, Waste Classification.

Font styles to use
Serif
Sans Serif

Requirements
Must have
• A creative design different to the standard type of business cards.
Nice to have
• Rounded edges
• Different size of business cards rather than the standard size.
Should not have
• Preferable not to use white colour background, unless it is required from a creative design proposed.
• Not an overloaded design.
• Avoid black colours

```html
<!DOCTYPE html>
<html lang="en">
<head>
<meta charset="utf-8">
<title>MOSLEN Environmental – Business Card</title>
<link rel="stylesheet" href="https://fonts.googleapis.com/css2?family=Sorts+Mill+Goudy&family=Roboto+Condensed:wght@700&display=swap">
<style>
  :root {
    --backdrop: #2f2a27;
    --card: #161716;
    --card-edge: #1d1f1c;
    --lime: #86c623;
    --band-top: #6aa41f;
    --band-bottom: #3f6e12;
    --text-light: #e6e6e6;
    --word-grey: #9c9c9c;
    --rule: #3c3d3b;
    --mark: #7fb52a;
  }
  * { box-sizing: border-box; margin: 0; padding: 0; }
  html, body { width: 1183px; height: 1200px; overflow: hidden; }
  body {
    background: var(--backdrop);
    position: relative;
    font-family: "Sorts Mill Goudy", Georgia, serif;
  }
  .card {
    position: absolute;
    left: 196px;
    width: 792px;
    height: 452px;
    background: linear-gradient(135deg, var(--card-edge), var(--card));
    border-radius: 14px;
    overflow: hidden;
  }
  .card--front { top: 121px; }
  .card--back { top: 626px; }

  .green-band {
    position: absolute;
    left: 0; right: 0; bottom: 0;
    background: linear-gradient(var(--band-top), var(--band-bottom));
  }
  .card--front .green-band { height: 46px; }
  .card--back .green-band {
    height: 74px;
    display: flex;
    flex-direction: column;
    justify-content: center;
    align-items: center;
    gap: 5px;
    color: var(--text-light);
    font-size: 16px;
  }
  .service-row span + span::before {
    content: "|";
    margin: 0 12px;
  }

  .acronym {
    position: absolute;
    left: 52px;
    top: 54px;
    list-style: none;
    font-family: "Roboto Condensed", Arial, sans-serif;
    font-weight: 700;
  }
  .acronym__row {
    display: flex;
    align-items: center;
    height: 49px;
  }
  .acronym__letter {
    width: 44px;
    text-align: center;
    font-size: 46px;
    line-height: 1;
    color: var(--mark);
  }
  .acronym__word {
    margin-left: 12px;
    font-size: 20px;
    color: var(--word-grey);
    letter-spacing: 0.2px;
  }

  .divider {
    position: absolute;
    left: 358px;
    top: 30px;
    width: 2px;
    height: 350px;
    background: var(--rule);
  }

  .contact {
    position: absolute;
    left: 383px;
    top: 44px;
    color: var(--text-light);
  }
  .contact__name { color: var(--lime); font-size: 36px; line-height: 1.1; }
  .contact__role { color: var(--lime); font-size: 27px; margin-top: 6px; }
  .contact__company { color: var(--lime); font-size: 24px; margin-top: 44px; }
  .contact__details { font-size: 17px; line-height: 1.3; margin-top: 8px; list-style: none; }
  .contact__details li { margin-bottom: 6px; }

  .brand {
    position: absolute;
    left: 0; right: 0;
    top: 120px;
    text-align: center;
    font-family: "Roboto Condensed", Arial, sans-serif;
    font-weight: 700;
    color: var(--mark);
  }
  .brand__name { font-size: 92px; line-height: 1; letter-spacing: 2px; }
  .brand__sub { font-size: 30px; letter-spacing: 6px; margin-top: 8px; }
</style>
</head>
<body>
  <section class="card card--front" aria-label="Business card front">
    <ul class="acronym" aria-label="MOSLEN acronym">
      <li class="acronym__row"><span class="acronym__letter">M</span><span class="acronym__word">ONITORING</span></li>
      <li class="acronym__row"><span class="acronym__letter">O</span><span class="acronym__word">F</span></li>
      <li class="acronym__row"><span class="acronym__letter">S</span><span class="acronym__word">OILS,</span></li>
      <li class="acronym__row"><span class="acronym__letter">L</span><span class="acronym__word">AND (AND)</span></li>
      <li class="acronym__row"><span class="acronym__letter">E</span><span class="acronym__word">COLOGICAL</span></li>
      <li class="acronym__row"><span class="acronym__letter">N</span><span class="acronym__word">ETWORKS</span></li>
    </ul>
    <div class="divider"></div>
    <div class="contact">
      <p class="contact__name">NAME</p>
      <p class="contact__role">Role</p>
      <p class="contact__company">MOSLEN Environmental</p>
      <ul class="contact__details">
        <li>A: Level 3, Suite 3C, 47-49 Dorrigan Lane,<br>Wexmoor, NSW, 2188</li>
        <li>L: 02 7314 2986<br>M: XXXX XXXX</li>
        <li>E: staff.member@moslengreen.example</li>
        <li>W: www.moslengreen.example</li>
      </ul>
    </div>
    <div class="green-band"></div>
  </section>

  <section class="card card--back" aria-label="Business card back">
    <div class="brand">
      <p class="brand__name">MOSLEN</p>
      <p class="brand__sub">ENVIRONMENTAL</p>
    </div>
    <div class="green-band">
      <p class="service-row"><span>Contaminated Land</span><span>Site Remediation</span><span>Groundwater Assessment</span></p>
      <p class="service-row"><span>Health and Ecological Risk Assessments</span><span>Acid Sulfate Soils</span><span>Waste Classification</span></p>
    </div>
  </section>
</body>
</html>
```